Business Card Design Project

We are an agricultural business based in Brisbane.
We design, manage and operate regional saleyards. Our logo is green/silver in colour and details of our business can be found on our website www.vodemarketyards.com.au

Just wanting a corporate design for some business cards and include name, position, contact details.

Thanks

Industry/Entity Type

Business

```html
<!DOCTYPE html>
<html lang="en">
<head>
<meta charset="utf-8">
<title>Vode Market Yards – Business Card</title>
<link rel="stylesheet" href="https://fonts.googleapis.com/css2?family=Oswald:wght@300;400;600&display=swap">
<style>
  :root {
    --paper: #ffffff;
    --ink: #1a1a1a;
    --frame: #3a3a3a;
    --green: #138a43;
    --silver: #939395;
    --silver-light: #a3a3a5;
    --label: #444444;
  }
  * { margin: 0; padding: 0; box-sizing: border-box; }
  html, body {
    width: 1200px;
    height: 927px;
    overflow: hidden;
    background: var(--paper);
    font-family: "Oswald", sans-serif;
  }
  .sheet { position: relative; width: 1200px; height: 927px; }
  .side-label {
    position: absolute;
    top: 280px;
    font-size: 14px;
    font-weight: 300;
    color: var(--label);
    letter-spacing: 0.5px;
    transform: translateX(-50%);
  }
  .side-label--front { left: 342px; }
  .side-label--back { left: 813px; }

  .card {
    position: absolute;
    top: 360px;
    width: 380px;
    height: 224px;
    border: 1.5px solid var(--frame);
    background: var(--paper);
    overflow: hidden;
  }
  .card--front { left: 178px; }
  .card--back { left: 632px; }

  .wordmark {
    position: absolute;
    left: 14px;
    top: 32px;
    display: flex;
    align-items: center;
    gap: 8px;
  }
  .wordmark__square {
    width: 14px;
    height: 14px;
    background: var(--green);
  }
  .wordmark__name {
    font-size: 22px;
    font-weight: 600;
    color: var(--ink);
    letter-spacing: 0.5px;
    text-transform: uppercase;
    line-height: 1;
  }

  .name-bar {
    position: absolute;
    left: 220px;
    top: 95px;
    width: 160px;
    height: 35px;
    background: var(--green);
    padding: 2px 6px 0 0;
    text-align: right;
    color: var(--ink);
  }
  .name-bar__name { font-size: 14px; font-weight: 400; line-height: 17px; }
  .name-bar__title { font-size: 10px; font-weight: 300; line-height: 12px; }

  .contact-bar {
    position: absolute;
    left: 220px;
    top: 144px;
    width: 160px;
    height: 35px;
    background: var(--silver);
    padding: 3px 6px 0 0;
    text-align: right;
    color: var(--paper);
    font-size: 10px;
    font-weight: 300;
    line-height: 14px;
    letter-spacing: 0.3px;
  }
  .contact-bar__email { font-size: 9.5px; }

  .rules { position: absolute; left: 0; bottom: 0; width: 100%; height: 24px; }
  .rule { position: absolute; left: 0; width: 100%; height: 2.5px; }
  .rule--green-top { top: 3px; background: var(--green); }
  .rule--silver { top: 10px; background: var(--silver); }
  .rule--green-bottom { top: 17px; background: var(--green); }

  .card--back .wordmark {
    left: 50%;
    top: 50%;
    transform: translate(-50%, -50%);
    gap: 12px;
  }
  .card--back .wordmark__square { width: 20px; height: 20px; background: var(--silver-light); }
  .card--back .wordmark__name { font-size: 34px; color: var(--silver-light); white-space: nowrap; }
</style>
</head>
<body>
  <main class="sheet">
    <p class="side-label side-label--front">Front</p>
    <p class="side-label side-label--back">Back</p>

    <section class="card card--front" aria-label="Business card front">
      <div class="wordmark">
        <span class="wordmark__square"></span>
        <span class="wordmark__name">Vode Market Yards</span>
      </div>

      <div class="name-bar">
        <p class="name-bar__name">Daniel Hartwell</p>
        <p class="name-bar__title">Chief Executive Officer</p>
      </div>

      <div class="contact-bar">
        <p class="contact-bar__email">Email: daniel@vodemarketyards.com.au</p>
        <p class="contact-bar__phone">P: 0412 555 019</p>
      </div>

      <div class="rules">
        <span class="rule rule--green-top"></span>
        <span class="rule rule--silver"></span>
        <span class="rule rule--green-bottom"></span>
      </div>
    </section>

    <section class="card card--back" aria-label="Business card back">
      <div class="wordmark">
        <span class="wordmark__square"></span>
        <span class="wordmark__name">Vode Market Yards</span>
      </div>
    </section>
  </main>
</body>
</html>
```